Folded A4 flyer for design&construction company

Folded A4 flyer needed. Keywords: elegant, stylish
our website www.dravimo.ae

Industry/Entity Type

Construction

```html
<!DOCTYPE html>
<html lang="en">
<head>
<meta charset="utf-8">
<title>Dravimo – Design &amp; Construction Flyer</title>
<link rel="stylesheet" href="https://fonts.googleapis.com/css2?family=Lato:wght@400;700&family=Montserrat:wght@400&family=Oswald:wght@500;600&display=swap">
<style>
  :root {
    --stage: #e4e4e4;
    --paper: #ffffff;
    --ink: #1c1c1c;
    --band: #1f1f1f;
    --band-text: #ffffff;
    --gold: #a98a2c;
    --body-text: #333333;
    --photo-warm-1: #f2a12a;
    --photo-warm-2: #c98a3c;
    --photo-pale-1: #f7f7f7;
    --photo-pale-2: #e9e9e9;
  }
  * { box-sizing: border-box; margin: 0; padding: 0; }
  html, body { width: 1200px; height: 847px; overflow: hidden; }
  body {
    background: var(--stage);
    font-family: "Lato", Arial, sans-serif;
    color: var(--ink);
    position: relative;
  }
  .flyer {
    position: absolute;
    left: 180px; top: 126px;
    width: 840px; height: 594px;
    display: flex;
    box-shadow: 0 10px 30px rgba(0,0,0,.18);
  }
  .panel {
    position: relative;
    width: 420px; height: 594px;
    background: var(--paper);
    overflow: hidden;
  }
  .panel--back { border-right: 1px solid #ececec; }

  .brand {
    display: flex; align-items: center; justify-content: center; gap: 8px;
    font-family: "Lato", Arial, sans-serif;
    font-weight: 700;
    color: var(--ink);
    letter-spacing: 2px;
  }
  .brand__mark { width: 10px; height: 10px; background: var(--gold); }

  /* back cover */
  .back-photo {
    position: absolute; left: 0; top: 0; width: 420px; height: 330px;
    background: linear-gradient(160deg, var(--photo-pale-2) 0%, var(--photo-pale-1) 55%, var(--paper) 100%);
  }
  .panel--back .brand { position: absolute; top: 352px; left: 0; right: 0; font-size: 34px; }
  .tagline {
    position: absolute; top: 420px; left: 0; right: 0;
    text-align: center;
    font-family: "Montserrat", Arial, sans-serif;
    font-size: 16.5px;
    color: var(--ink);
  }

  /* front cover */
  .panel--front .brand { position: absolute; top: 36px; left: 0; right: 0; font-size: 30px; }
  .front-photo {
    position: absolute; left: 16px; top: 98px; width: 388px; height: 196px;
    background: linear-gradient(135deg, #f6f1e8 0%, var(--photo-warm-1) 40%, #ffffff 55%, var(--photo-warm-2) 100%);
  }
  .intro {
    position: absolute; left: 16px; top: 310px; width: 388px;
    font-size: 8.3px; line-height: 1.38;
    color: var(--body-text);
  }
  .cta {
    position: absolute; left: 16px; top: 388px;
    font-family: "Oswald", Arial, sans-serif; font-weight: 600;
    font-size: 18px; color: var(--gold);
    letter-spacing: .3px;
  }
  .contact { position: absolute; right: 18px; top: 372px; text-align: left; }
  .contact__phone { font-weight: 700; font-size: 18px; color: var(--ink); }
  .contact__email { font-size: 13px; color: var(--ink); margin-top: 2px; }

  .band {
    position: absolute; left: 0; bottom: 0; width: 100%; height: 62px;
    background: var(--band);
    color: var(--band-text);
    display: flex; flex-direction: column; align-items: center; justify-content: flex-start;
    padding-top: 6px;
    background-clip: padding-box;
  }
  .band--top-white { border-top: 0; }
  .band__web { font-size: 11px; }
  .band__address { font-size: 11px; margin-top: 2px; }
  .footer-strip {
    position: absolute; left: 0; bottom: 0; width: 100%; height: 98px;
    background: linear-gradient(var(--paper) 0 40px, var(--band) 40px);
  }
  .footer-text {
    position: absolute; left: 0; right: 0; bottom: 62px;
    text-align: center; color: var(--ink); font-size: 11.5px; line-height: 1.35;
  }
  .footer-text.on-band { bottom: 22px; color: var(--band-text); }
</style>
</head>
<body>
  <main class="flyer">
    <section class="panel panel--back">
      <div class="back-photo" role="img" aria-label="Faded photo of a bright white modern living room with tall windows"></div>
      <div class="brand"><span class="brand__mark"></span>DRAVIMO</div>
      <p class="tagline">Quality is not an act, it is a habit – Theron Vale</p>
      <div class="footer-strip"></div>
      <p class="footer-text on-band">www.dravimo.ae<br>Dravimo LLC, Palm Crest Tower, Office 902, Marina Row, Dubai</p>
    </section>

    <section class="panel panel--front">
      <div class="brand"><span class="brand__mark"></span>DRAVIMO</div>
      <div class="front-photo" role="img" aria-label="Photo of a modern interior with an orange curved ceiling, spiral staircase and wooden floor"></div>
      <p class="intro">We believe in quality beginnings and flawless finishes. We are a team of creative designers and constructors with years of experience and expertise in providing complete interior design and construction services. Our unique designing prowess is complemented by our unflinching commitment to quality construction. Our team specializes in classic and contemporary high quality construction in Dubai for commercial and residential projects.</p>
      <p class="cta">GET A FREE QUOTE TODAY!</p>
      <div class="contact">
        <p class="contact__phone">800 – 4826</p>
        <p class="contact__email">contact@dravimo.ae</p>
      </div>
      <div class="footer-strip"></div>
      <p class="footer-text on-band">www.dravimo.ae<br>Dravimo LLC, Palm Crest Tower, Office 902, Marina Row, Dubai</p>
    </section>
  </main>
</body>
</html>
```